Creative lead conversion landing page for SMBs

We have an AI chatbot webpage for a real estate agent, and we’re are going to start sending traffic to that webpage (primarily from Zintavo)
We want to maximize the percentage of visitors who start conversations with the chatbot.
We have a specific area of the webpage where we can include any HTML.
We need the design and HTML for both desktop and mobile version.
We’re looking for the best designs that help convert visitors into people who engage the chatbot.

Details are in the attached document "Pitchforge project for chat conversion". Please let me know if you have any questions!

Target Market(s)

SMBs (think real estate agents, or home services like tree care, housekeepers, electricians, general contractors) will be selling to consumers

Number of Pages Required

1 page

Font styles to use
Other font styles liked:
• Zintavo Poppins

Requirements
Must have
• Creative design that catches users eyes and with good content (content of course out of scope) will encourage a user to want to learn more.

```html
<!DOCTYPE html>
<html lang="en">
<head>
<meta charset="utf-8">
<title>Marisa – Real Estate Agent | Chat with Nova</title>
<link rel="stylesheet" href="https://fonts.googleapis.com/css2?family=Poppins:wght@400;500;600;700&display=swap">
<style>
  :root {
    --teal: #2aa3b3;
    --teal-dark: #1f8c9b;
    --ink: #2b2f36;
    --muted: #6b7079;
    --page: #ffffff;
    --stage: #eef1f4;
    --bubble: #ffffff;
    --input: #e6e7ea;
    --navy: #13243a;
    --gold: #f5b82e;
    --photo-warm: #c9b9a6;
    --photo-cool: #9fb3c4;
  }
  * { box-sizing: border-box; margin: 0; padding: 0; }
  html, body { width: 670px; height: 1200px; overflow: hidden; }
  body {
    font-family: "Poppins", sans-serif;
    background: var(--page);
    color: var(--ink);
    position: relative;
  }

  /* Agent header */
  .agent-header {
    display: flex;
    align-items: center;
    gap: 34px;
    padding: 44px 40px 0;
    height: 214px;
  }
  .agent-avatar {
    width: 140px; height: 140px;
    border-radius: 50%;
    border: 5px solid var(--teal);
    padding: 4px;
    flex: none;
  }
  .agent-avatar span {
    display: block; width: 100%; height: 100%;
    border-radius: 50%;
    background: linear-gradient(160deg, #5a4236, #b88e74);
  }
  .agent-name { font-size: 42px; font-weight: 500; line-height: 1.1; }
  .agent-role { font-size: 22px; color: var(--muted); margin-top: 6px; }
  .agent-cta { font-size: 22px; color: var(--teal); margin-top: 14px; }
  .scroll-hint { display: block; margin: 0 auto; }

  /* Profile card */
  .profile-card {
    margin: 10px 16px 0;
    background: var(--teal);
    border-radius: 18px;
    color: #fff;
    padding: 24px 28px 26px;
  }
  .profile-top { display: flex; gap: 26px; }
  .profile-avatar {
    width: 118px; height: 118px; flex: none;
    border-radius: 50%;
    border: 4px solid #fff;
    background: linear-gradient(160deg, #5a4236, #b88e74);
  }
  .profile-name { font-size: 30px; font-weight: 700; margin-bottom: 6px; }
  .profile-cols { display: flex; gap: 22px; }
  .profile-col h3 { font-size: 17px; font-weight: 600; }
  .profile-col p { font-size: 12px; line-height: 1.55; opacity: .95; }
  .profile-col.specialties { width: 170px; }
  .profile-col.about { flex: 1; }

  .section-title {
    text-align: center;
    font-size: 26px;
    font-weight: 600;
    margin-top: 14px;
    padding-bottom: 6px;
    position: relative;
  }
  .section-title::after {
    content: ""; display: block;
    width: 300px; height: 2px; background: #fff;
    margin: 4px auto 0;
  }
  .testimonial { display: flex; align-items: center; gap: 12px; margin-top: 8px; }
  .testimonial-quote { flex: 1; font-size: 13px; line-height: 1.55; text-align: center; }
  .stars { color: var(--gold); font-size: 18px; letter-spacing: 2px; text-align: center; margin-top: 4px; }
  .reviewer { text-align: center; font-size: 15px; font-weight: 600; }

  .gallery { display: flex; gap: 12px; margin-top: 10px; }
  .gallery-item { flex: 1; height: 92px; border-radius: 6px; }
  .gallery-item.house { background: linear-gradient(180deg, #7fa6cf, #8a7a5e); }
  .gallery-item.meeting { background: linear-gradient(160deg, #e9e3da, var(--photo-warm)); }
  .gallery-item.keys { background: linear-gradient(160deg, #d8dde2, var(--photo-cool)); }
  .gallery-item.couple { background: linear-gradient(160deg, #b8b1a8, #6d6257); }

  /* Chat */
  .chat { padding: 24px 40px 0; }
  .chat-bubble {
    width: 380px;
    background: var(--bubble);
    border-radius: 18px;
    box-shadow: 0 3px 14px rgba(0,0,0,.14);
    padding: 20px 22px;
    font-size: 18px;
    line-height: 1.5;
  }
  .assistant-mascot {
    width: 82px; height: 96px; margin-top: 16px;
    border-radius: 40px 40px 30px 30px;
    background: linear-gradient(180deg, #7fd3dc, var(--teal));
  }
  .chat-input {
    margin: 20px 40px 0;
    height: 66px;
    background: var(--input);
    border-radius: 6px;
    padding: 0 22px;
    display: flex; align-items: center;
    font-size: 19px; color: var(--muted);
  }

  /* Footer */
  .site-footer {
    position: absolute; left: 0; right: 0; bottom: 0;
    height: 78px;
    background: var(--navy);
    display: flex; align-items: center; justify-content: space-between;
    padding: 0 40px;
  }
  .create-button {
    background: var(--teal);
    color: #fff;
    font-size: 19px;
    font-weight: 500;
    padding: 10px 28px;
    border-radius: 30px;
  }
  .brand-name { color: #fff; font-size: 32px; font-weight: 700; }
</style>
</head>
<body>
  <header class="agent-header">
    <div class="agent-avatar"><span role="img" aria-label="Portrait photo of the agent Marisa"></span></div>
    <div>
      <h1 class="agent-name">Marisa</h1>
      <p class="agent-role">Real Estate Agent</p>
      <p class="agent-cta">Talk to Nova, my AI assistant.</p>
    </div>
  </header>
  <svg class="scroll-hint" width="30" height="20" viewBox="0 0 30 20" aria-hidden="true">
    <path d="M4 4 L15 15 L26 4" fill="none" stroke="#2b2f36" stroke-width="4" stroke-linecap="round" stroke-linejoin="round"/>
  </svg>

  <section class="profile-card">
    <div class="profile-top">
      <div class="profile-avatar" role="img" aria-label="Portrait photo of the agent Marisa"></div>
      <div>
        <h2 class="profile-name">Marisa J. Caldwell</h2>
        <div class="profile-cols">
          <div class="profile-col specialties">
            <h3>Specialties</h3>
            <p>BR, OTHR, LUX, SL, RA, INV, CON, MIL, NEW, FL, RELO</p>
          </div>
          <div class="profile-col about">
            <h3>About Us</h3>
            <p>Hi! I am Marisa. Buying or Selling a home is a big decision and</p>
          </div>
        </div>
      </div>
    </div>

    <h2 class="section-title">Testimonials</h2>
    <div class="testimonial">
      <svg width="16" height="16" viewBox="0 0 16 16" aria-hidden="true"><circle cx="8" cy="8" r="8" fill="#fff"/><path d="M10 4 L6 8 L10 12" fill="none" stroke="#2aa3b3" stroke-width="2"/></svg>
      <p class="testimonial-quote">Marisa is the best! She was extremely helpful to me and my girlfriend as First-time Home Buyers. She made the whole process super easy and</p>
      <svg width="16" height="16" viewBox="0 0 16 16" aria-hidden="true"><circle cx="8" cy="8" r="8" fill="#fff"/><path d="M6 4 L10 8 L6 12" fill="none" stroke="#2aa3b3" stroke-width="2"/></svg>
    </div>
    <p class="stars">★★★★★</p>
    <p class="reviewer">Daniel and Priya</p>

    <h2 class="section-title">Our Gallery</h2>
    <div class="gallery">
      <div class="gallery-item house" role="img" aria-label="Photo of a suburban house exterior"></div>
      <div class="gallery-item meeting" role="img" aria-label="Photo of an agent meeting clients"></div>
      <div class="gallery-item keys" role="img" aria-label="Photo of a key handover"></div>
      <div class="gallery-item couple" role="img" aria-label="Photo of a couple in their new home"></div>
    </div>
  </section>

  <section class="chat">
    <p class="chat-bubble">Hi! I'm the AI assistant to Marisa, who can help you buy or sell a home in the Indianapolis area. I am happy to help get you connected to her. First, what's your name?</p>
    <div class="assistant-mascot" role="img" aria-label="Illustrated owl mascot of the Nova assistant"></div>
  </section>
  <div class="chat-input">Type your response...</div>

  <footer class="site-footer">
    <span class="create-button">Create your own</span>
    <span class="brand-name">askNova</span>
  </footer>
</body>
</html>
```